Broschüre für Kindertagesstätte
Zielgruppe
Wir sind eine Kindertagesstätte für Kinder ab 10 Monate mit Öffnungszeiten von 06.00 Uhr bis 19.00 Uhr
Aufgabenstellung
bitte Klappflyer gestalten, Eltern-Kind-Spielgruppe bitte im Flyer extra gestalten. Bitte hervorheben, dass wir eine hauseigene Kita-Küche haben, in der täglich frisch für unsere Kinder gekocht wird.

```html
<!DOCTYPE html>
<html lang="de">
<head>
<meta charset="utf-8">
<title>Kita Klappflyer – Innenseiten</title>
<link href="https://fonts.googleapis.com/css2?family=Oswald:wght@300;400&family=Source+Sans+3:wght@400;600&display=swap" rel="stylesheet">
<style>
  :root {
    --stage: #c3c3c3;
    --paper: #f1edea;
    --ink: #555050;
    --heading: #4d4a4a;
    --accent: #dc6a35;
    --icon-tile: #7d7677;
    --divider: #4a4a4a;
    --band-purple: #8b76a8;
    --band-green: #8db544;
    --band-yellow: #edb43b;
    --band-blue: #1e9ad6;
    --band-red: #b6302a;
    --white: #ffffff;
  }
  * { margin: 0; padding: 0; box-sizing: border-box; }
  html, body { width: 1200px; height: 1192px; overflow: hidden; background: var(--stage); }
  .spread {
    position: absolute; left: 27px; top: 15px; width: 1158px; height: 1156px;
    background: var(--paper);
  }
  .panel { position: absolute; top: 0; height: 100%; }
  .panel--left { left: 0; width: 581px; border-right: 2px solid var(--divider); }
  .panel--right { left: 581px; width: 577px; }
  .photo { position: absolute; left: 0; top: 0; width: 100%; height: 385px; }
  .photo--blocks { background: linear-gradient(135deg, #a39a94 0%, #d8cfc7 45%, #c9674a 75%, #e9e2dc 100%); }
  .photo--hall { background: linear-gradient(180deg, #d9d6cf 0%, #d49a3a 45%, #b5782d 75%, #c8863a 100%); }
  .section-title {
    position: absolute; top: 440px;
    font-family: "Oswald", sans-serif; font-weight: 300; font-size: 37px; line-height: 52px;
    color: var(--heading); letter-spacing: 0.5px; white-space: nowrap;
  }
  .panel--left .section-title { left: 62px; }
  .panel--right .section-title { left: 60px; }
  .title-rule { position: absolute; top: 509px; left: 0; height: 5px; background: var(--accent); border-radius: 0 3px 3px 0; }
  .panel--left .title-rule { width: 399px; }
  .panel--right .title-rule { width: 338px; }
  .feature { position: absolute; left: 61px; display: flex; gap: 19px; }
  .feature__icon {
    width: 82px; height: 82px; border-radius: 14px; background: var(--icon-tile);
    flex: none; display: flex; align-items: center; justify-content: center;
  }
  .feature__text {
    font-family: "Source Sans 3", sans-serif; font-size: 21px; line-height: 34.5px;
    color: var(--ink); margin-top: -6px;
  }
  .checklist { position: absolute; left: 58px; top: 531px; list-style: none; }
  .checklist li {
    display: flex; align-items: center; gap: 15px; height: 35px;
    font-family: "Source Sans 3", sans-serif; font-size: 21px; color: var(--ink);
  }
  .quote-box {
    position: absolute; left: 31px; top: 788px; width: 527px; height: 307px;
    background: var(--accent); border-radius: 70px 6px 70px 6px;
    padding: 40px 40px 0 49px; color: var(--white);
  }
  .quote-box blockquote {
    font-family: "Oswald", sans-serif; font-weight: 400; font-size: 34px; line-height: 44px;
    letter-spacing: 0.3px;
  }
  .quote-box cite {
    display: block; margin-top: 32px; font-style: normal;
    font-family: "Source Sans 3", sans-serif; font-weight: 600; font-size: 17px;
  }
  .color-band { position: absolute; left: 0; bottom: 0; width: 100%; height: 18px; display: flex; }
  .color-band span { height: 100%; }
</style>
</head>
<body>
<main class="spread">
  <section class="panel panel--left">
    <div class="photo photo--blocks" role="img" aria-label="Kinderhand stapelt bunte Bausteine"></div>
    <h2 class="section-title">Das ist besonders bei uns</h2>
    <div class="title-rule"></div>

    <div class="feature" style="top:537px">
      <div class="feature__icon">
        <svg width="54" height="54" viewBox="0 0 54 54" fill="none" stroke="#fff" stroke-width="3" stroke-linecap="round"><circle cx="27" cy="27" r="22"/><path d="M27 13v14l9 8"/></svg>
      </div>
      <p class="feature__text">lange Öffnungszeiten<br>(06.00 bis 19.00 Uhr)<br>flexible Bring- und Abholzeiten</p>
    </div>

    <div class="feature" style="top:678px">
      <div class="feature__icon">
        <svg width="54" height="54" viewBox="0 0 54 54" fill="none" stroke="#fff" stroke-width="3" stroke-linecap="round"><rect x="6" y="10" width="42" height="38" rx="3"/><path d="M6 21h42M16 5v10M38 5v10"/></svg>
      </div>
      <p class="feature__text">ganzjährige Aufnahme<br>keine betriebsbedingten Schließ-<br>zeiten</p>
    </div>

    <div class="feature" style="top:815px">
      <div class="feature__icon">
        <svg width="56" height="56" viewBox="0 0 56 56" fill="none" stroke="#fff" stroke-width="3" stroke-linecap="round"><path d="M10 24h36v20a6 6 0 0 1-6 6H16a6 6 0 0 1-6-6z"/><path d="M4 27h6M46 27h6M8 20h40"/><path d="M20 14l16-8"/><circle cx="42" cy="10" r="2"/><circle cx="46" cy="16" r="1.5"/></svg>
      </div>
      <p class="feature__text">Gesunde Ernährung von Anfang an<br>aus unserer eigenen Kita-Küche</p>
    </div>

    <div class="feature" style="top:952px">
      <div class="feature__icon">
        <svg width="54" height="54" viewBox="0 0 54 54" fill="none" stroke="#fff" stroke-width="3" stroke-linejoin="round"><path d="M27 46S7 33 7 19a10 10 0 0 1 20-3 10 10 0 0 1 20 3c0 14-20 27-20 27z"/></svg>
      </div>
      <p class="feature__text">große Turn- und Bewegungshalle<br>großzügige Räume für individuelle<br>Bildungschancen</p>
    </div>
  </section>

  <section class="panel panel--right">
    <div class="photo photo--hall" role="img" aria-label="Helle Turnhalle mit Rutsche, Kästen und Bällen"></div>
    <h2 class="section-title">Weitere Einrichtungen für Ihr Kind</h2>
    <div class="title-rule"></div>

    <ul class="checklist">
      <li><svg width="20" height="16" viewBox="0 0 20 16"><path d="M2 8l5 5L18 2" fill="none" stroke="#555050" stroke-width="3"/></svg>Kindersauna</li>
      <li><svg width="20" height="16" viewBox="0 0 20 16"><path d="M2 8l5 5L18 2" fill="none" stroke="#555050" stroke-width="3"/></svg>2 Außenbereiche</li>
      <li><svg width="20" height="16" viewBox="0 0 20 16"><path d="M2 8l5 5L18 2" fill="none" stroke="#555050" stroke-width="3"/></svg>Logo- und Ergotherapie möglich</li>
      <li><svg width="20" height="16" viewBox="0 0 20 16"><path d="M2 8l5 5L18 2" fill="none" stroke="#555050" stroke-width="3"/></svg>Turn- und Bewegungshalle</li>
      <li><svg width="20" height="16" viewBox="0 0 20 16"><path d="M2 8l5 5L18 2" fill="none" stroke="#555050" stroke-width="3"/></svg>kostenfreie Schnuppertage</li>
      <li><svg width="20" height="16" viewBox="0 0 20 16"><path d="M2 8l5 5L18 2" fill="none" stroke="#555050" stroke-width="3"/></svg>uvm.</li>
    </ul>

    <figure class="quote-box">
      <blockquote>„Kinder brauchen Zeit, Platz<br>und Begleitung auf ihrem<br>individuellen Entwicklungsweg!“</blockquote>
      <cite>Katharina Wendlin, Sozialpädagogin, Kita Leiterin</cite>
    </figure>
  </section>

  <div class="color-band">
    <span style="width:224px;background:var(--band-purple)"></span>
    <span style="width:236px;background:var(--band-green)"></span>
    <span style="width:243px;background:var(--band-yellow)"></span>
    <span style="width:236px;background:var(--band-blue)"></span>
    <span style="width:219px;background:var(--band-red)"></span>
  </div>
</main>
</body>
</html>
```